We need business cards for our Kashmiri Indian Takeaway Shop. our business sells authentic Kashmiri Cuisine. We also offer catering services and have a BYO Function Room available for private bookings. We would like to see simple but stylish designs that feature Moroccan or Arabic style patterns/ borders and use golds, deep reds, pearl/cream and a touch of black or white. We do not want pictures of curries or Indian spices, chillies etc. The final design should communicate sumptuous, exotic dining.

Target Market(s)

Indian food lovers

Industry/Entity Type

Catering

Contact Information for Business Card

Rafi's Kitchen Authentic Kashmiri Indian Cuisine

Colors
ec2027
fce8d3
fcca95
faa54b

Requirements
Must have
• Simple but stylish design, using Moroccan/Arabic inspired borders or features
Should not have
• Pictures of curries, spices, food etc

```html
<!DOCTYPE html>
<html lang="en">
<head>
<meta charset="utf-8">
<title>Rafi's Kitchen – Business Card</title>
<link rel="stylesheet" href="https://fonts.googleapis.com/css2?family=Inter:wght@300;400&display=swap">
<style>
  :root {
    --page-bg: #f0f0f0;
    --cream: #fce8d3;
    --peach: #fcca95;
    --saffron: #faa54b;
    --chilli-red: #ec2027;
    --ink: #1a1a1a;
  }
  * { margin: 0; padding: 0; box-sizing: border-box; }
  html, body {
    width: 846px;
    height: 1200px;
    overflow: hidden;
    background: var(--page-bg);
    font-family: "Inter", "Helvetica Neue", Arial, sans-serif;
  }
  .canvas {
    position: relative;
    width: 846px;
    height: 1200px;
  }
  .card {
    position: absolute;
    left: 223px;
    top: 251px;
    width: 399px;
    height: 697px;
    border: 1px solid var(--peach);
    overflow: hidden;
  }
  .card-top {
    position: absolute;
    left: 0; top: 0;
    width: 100%;
    height: 402px;
    background: var(--cream);
  }
  .card-bottom {
    position: absolute;
    left: 0; top: 402px;
    width: 100%;
    height: 295px;
    background: var(--saffron);
    color: var(--ink);
    text-align: center;
  }
  .ornament {
    position: absolute;
    left: 122px;
    width: 154px;
    height: 50px;
    display: block;
  }
  .ornament-top { top: 86px; }
  .ornament-bottom { top: 243px; }
  .brand-name {
    position: absolute;
    left: 0; width: 100%;
    top: 160px;
    text-align: center;
    font-size: 34px;
    font-weight: 400;
    color: var(--chilli-red);
    letter-spacing: 0.5px;
    line-height: 1.2;
  }
  .tagline {
    position: absolute;
    left: 0; width: 100%;
    top: 206px;
    text-align: center;
    font-size: 19px;
    font-weight: 400;
    color: var(--ink);
    line-height: 1.2;
  }
  .owner-name {
    position: absolute;
    left: 0; width: 100%;
    top: 92px;
    font-size: 26px;
    font-weight: 300;
    line-height: 1.2;
  }
  .owner-role {
    position: absolute;
    left: 0; width: 100%;
    top: 131px;
    font-size: 14px;
    font-weight: 300;
  }
  .details {
    position: absolute;
    left: 0; width: 100%;
    top: 208px;
    font-size: 15px;
    font-weight: 300;
    line-height: 20px;
  }
</style>
</head>
<body>
<div class="canvas">
  <div class="card">
    <section class="card-top">
      <svg class="ornament ornament-top" viewBox="0 0 154 50" role="img" aria-label="Arabesque scroll ornament in saffron orange">
        <rect width="154" height="50" rx="6" fill="#faa54b" opacity="0.55"/>
      </svg>
      <h1 class="brand-name">Rafi's Kitchen</h1>
      <p class="tagline">Authentic Kashmiri Indian Cuisine</p>
      <svg class="ornament ornament-bottom" viewBox="0 0 154 50" role="img" aria-label="Arabesque scroll ornament in saffron orange">
        <rect width="154" height="50" rx="6" fill="#faa54b" opacity="0.55"/>
      </svg>
    </section>
    <section class="card-bottom">
      <p class="owner-name">Samir Qadri</p>
      <p class="owner-role">Owner &amp; Chef</p>
      <p class="details">
        Takeaway Shop &amp; Catering,<br>
        BYO Function Room - bookings essential<br>
        14B Maple Lane, Kenwood Qld, 07- 5550 1842
      </p>
    </section>
  </div>
</div>
</body>
</html>
```